Cause bitches need love too!

I am creating an ad campaign. It will be a series of featured dogs in our shelter and they will contain a picture of the dog wich should be big enough to see on a yard sign and will change every week. I am placing the signs so that they lead you to the shelter. This is why I am also including the copy that says "you're almost there".

I have 4 tag lines:

1. Find unconditional Love.
2. She'll Love you furever!
3. He'll always listen.
4. Meet your new BFF

You're almost there 318 W Harrowgate Ln
Open 10 - 7/Tues-Sat

The dimensions for the sign are 24" wide and 18" high

Every week we will have a different picture of a different dog (hopefully last week's dog gets adopted). Anyhow, I am printing out yard signs, meaning that instead of printing 160 different signs it would be ideal just to replace the photo. So far the copy that is permanent is: "You're almost there. 318 W. Harrowgate Ln."

I could silhouette the image of the dog as well and super impose it on the sign, that's also a consideration, but ideally if I could have 4 tag lines I could print 40 signs of each and just replace the photo manually each week from my printer that would save costs.
Updates

Not enough designs to chose from and I edited the brief and committed to pay no matter what to increase the amount of designs as per your suggestions.

Target Market(s)

Animal lovers

Industry/Entity Type

Campaign

Font styles to use
Sans Serif

Colors

Designer to choose colors to be used in the design.

Requirements
Must have
• The dimensions for the sign are 24" wide and 18" high
Nice to have
• I want the signs to be hip, they should have a positive feel to them. You can alter the photos if you like. I am even open to new copy if you think something else works better.

```html
<!DOCTYPE html>
<html lang="en">
<head>
<meta charset="utf-8">
<title>Shelter Yard Sign Series</title>
<link rel="stylesheet" href="https://fonts.googleapis.com/css2?family=Open+Sans:wght@300;400;700;800&display=swap">
<style>
  :root {
    --page-bg: #c8c5c4;
    --photo-bg-light: #dcd7d5;
    --photo-bg-dark: #c4bfbe;
    --band-bg: #ffffff;
    --ink: #1c1c1c;
    --headline: #ffffff;
    --headline-shadow: #1e1e1e;
  }
  * { box-sizing: border-box; margin: 0; padding: 0; }
  html, body {
    width: 690px;
    height: 1200px;
    overflow: hidden;
    background: var(--page-bg);
    font-family: "Open Sans", Arial, sans-serif;
  }
  .canvas {
    position: relative;
    width: 690px;
    height: 1200px;
  }
  .yard-sign {
    position: absolute;
    left: 143px;
    width: 386px;
    height: 289px;
    background: var(--band-bg);
    overflow: hidden;
  }
  .yard-sign--listen { top: 39px; }
  .yard-sign--furever { top: 423px; }
  .yard-sign--bff { top: 820px; }

  .photo-area {
    position: absolute;
    left: 0;
    top: 0;
    width: 386px;
    height: 223px;
    background: linear-gradient(135deg, var(--photo-bg-light), var(--photo-bg-dark));
    overflow: hidden;
  }
  .featured-dog {
    position: absolute;
    left: 0;
    bottom: 0;
  }
  .featured-dog--shepherd {
    width: 165px;
    height: 223px;
    background: linear-gradient(160deg, #c99a55 0%, #a87a3c 45%, #3a2a1c 100%);
    border-radius: 0 60% 0 0 / 0 30% 0 0;
  }
  .featured-dog--doodle {
    width: 220px;
    height: 210px;
    background: linear-gradient(150deg, #d9d9d6 0%, #b5b6b3 60%, #8e8f8c 100%);
    border-radius: 0 45% 0 0 / 0 35% 0 0;
  }
  .featured-dog--pitbull {
    width: 275px;
    height: 219px;
    background: linear-gradient(160deg, #a8948a 0%, #8c776c 55%, #6e5c53 100%);
    border-radius: 18% 40% 0 0 / 22% 30% 0 0;
  }

  .headline {
    position: absolute;
    right: 11px;
    bottom: -2px;
    text-align: right;
    text-transform: uppercase;
    font-weight: 800;
    color: var(--headline);
    letter-spacing: -1px;
    line-height: 0.84;
    text-shadow: -3px 2px 0 var(--headline-shadow);
  }
  .headline span { display: block; }
  .headline--listen .line-1,
  .headline--listen .line-2 { font-size: 52px; }
  .headline--listen .line-3 { font-size: 74px; }
  .headline--furever .line-1,
  .headline--furever .line-2 { font-size: 46px; }
  .headline--furever .line-3 { font-size: 64px; }
  .headline--bff .line-1 { font-size: 46px; }
  .headline--bff .line-2,
  .headline--bff .line-3 { font-size: 58px; }

  .info-band {
    position: absolute;
    left: 0;
    top: 223px;
    width: 386px;
    height: 66px;
    background: var(--band-bg);
    color: var(--ink);
    text-align: center;
    text-transform: uppercase;
    display: flex;
    flex-direction: column;
    justify-content: center;
  }
  .info-band .address {
    font-weight: 800;
    line-height: 1.1;
  }
  .info-band .hours {
    font-weight: 300;
    font-size: 19px;
    line-height: 1.15;
  }
  .info-band--wayfinding .address { font-size: 16px; }
  .info-band--destination .address { font-size: 24px; }
</style>
</head>
<body>
<main class="canvas">

  <section class="yard-sign yard-sign--listen">
    <div class="photo-area">
      <div class="featured-dog featured-dog--shepherd" role="img" aria-label="Featured shelter dog: tan and black shepherd mix tilting its head"></div>
      <h2 class="headline headline--listen">
        <span class="line-1">He'll</span>
        <span class="line-2">Always</span>
        <span class="line-3">Listen</span>
      </h2>
    </div>
    <div class="info-band info-band--wayfinding">
      <p class="address">Almost there: 318 W Harrowgate Ln</p>
      <p class="hours">Open Tuesday-Sunday till 7pm</p>
    </div>
  </section>

  <section class="yard-sign yard-sign--furever">
    <div class="photo-area">
      <div class="featured-dog featured-dog--doodle" role="img" aria-label="Featured shelter dog: curly grey doodle holding a red rose in its mouth"></div>
      <h2 class="headline headline--furever">
        <span class="line-1">She'll</span>
        <span class="line-2">Love you</span>
        <span class="line-3">Furever!</span>
      </h2>
    </div>
    <div class="info-band info-band--destination">
      <p class="address">318 W Harrowgate Ln</p>
      <p class="hours">Open Tuesday-Sunday till 7pm</p>
    </div>
  </section>

  <section class="yard-sign yard-sign--bff">
    <div class="photo-area">
      <div class="featured-dog featured-dog--pitbull" role="img" aria-label="Featured shelter dog: grey and white pit bull looking up"></div>
      <h2 class="headline headline--bff">
        <span class="line-1">Meet</span>
        <span class="line-2">Your</span>
        <span class="line-3">New BFF</span>
      </h2>
    </div>
    <div class="info-band info-band--destination">
      <p class="address">318 W Harrowgate Ln</p>
      <p class="hours">Open Tuesday-Sunday till 7pm</p>
    </div>
  </section>

</main>
</body>
</html>
```